Looking for a website design for my company
Services we offer:
Phone Repair
TV Mounting
Security Camera Installation
Networking / Wi-Fi
Smart Home Services
IT Support

Looking for a website similar to kevra.com

Few tabs
About Us
Contact Us
Areas Served
Pricing and Services

```html
<!DOCTYPE html>
<html lang="en">
<head>
<meta charset="utf-8">
<title>Bolt Handy — Installation, Repairs and Smart Home</title>
<link href="https://fonts.googleapis.com/css2?family=Poppins:ital,wght@1,800&family=Roboto:ital,wght@0,400;0,500;0,700;1,400;1,500&family=Roboto+Condensed:ital,wght@1,400;1,700&display=swap" rel="stylesheet">
<style>
:root{
  --orange:#f7941d;
  --ink:#1f1f1f;
  --text:#555;
  --muted:#7a7a7a;
  --line:#e3e3e3;
  --cream:#fdf4ec;
  --mist:#f4f4f4;
  --footer:#2e3033;
  --white:#fff;
}
*{margin:0;padding:0;box-sizing:border-box}
html,body{width:1200px;height:3929px;overflow:hidden}
body{position:relative;background:var(--white);font-family:'Roboto',sans-serif;color:var(--text)}
.abs{position:absolute}
a{color:inherit;text-decoration:none}

/* header */
.site-header{left:0;top:0;width:1200px;height:64px;background:var(--white);border-bottom:2px solid #ececec;z-index:5}
.brand{left:142px;top:14px;display:flex;align-items:center;gap:9px;font-family:'Roboto',sans-serif;font-weight:700;font-style:normal;font-size:30px;color:var(--orange);letter-spacing:-.3px}
.brand-mark{width:12px;height:12px;background:var(--orange)}
.nav{top:34px;font-size:14px;font-style:italic;color:#777}
.nav.active{color:var(--orange)}

/* hero */
.hero-bg{left:0;top:64px;width:1200px;height:580px;background:linear-gradient(90deg,#f5f6f7 0%,#f1f1f0 40%,#ede4d8 100%);clip-path:polygon(0 0,100% 0,100% 92%,0 100%)}
.hero-photo{left:520px;top:64px;width:680px;height:550px;background:linear-gradient(160deg,#e7d6c2 0%,#d9b794 45%,#b38860 100%);clip-path:polygon(12% 0,100% 0,100% 100%,0 100%,0 70%);opacity:.85}
.hero-title{left:142px;top:220px;font-family:'Poppins',sans-serif;font-style:italic;font-weight:800;font-size:43px;line-height:51px;color:#111}
.btn{background:var(--orange);color:var(--white);font-weight:500;display:flex;align-items:center;justify-content:center}
.hero-btn{left:142px;top:392px;width:169px;height:52px;font-size:18px}

/* services */
.services{left:142px;top:582px;width:918px;height:127px;background:var(--white);border-radius:6px;box-shadow:0 4px 16px rgba(0,0,0,.12);display:flex;z-index:3}
.service{flex:1;display:flex;flex-direction:column;align-items:center;justify-content:flex-start;padding-top:22px;font-size:13.5px;color:#666;text-align:center;line-height:17px;border-right:1px solid var(--line);margin:14px 0}
.service:last-child{border-right:none}
.service svg{width:46px;height:46px;margin-bottom:14px;margin-top:-10px}
.service.current{color:var(--orange)}

/* about */
.house-photo{left:142px;top:796px;width:564px;height:424px;background:linear-gradient(180deg,#c9d8e6 0%,#b9b3a6 45%,#6d7f4a 75%,#5d8a33 100%)}
.about-card{left:622px;top:833px;width:438px;height:352px;background:var(--white);box-shadow:0 4px 20px rgba(0,0,0,.08);padding:64px 56px}
.section-title{font-family:'Roboto Condensed',sans-serif;font-style:italic;font-weight:400;color:#666;font-size:31px}
.about-card h2{line-height:40px;margin-bottom:22px}
.ticks{list-style:none}
.ticks li{position:relative;padding-left:28px;font-size:13.5px;line-height:20px;color:#777;margin-bottom:12px}
.ticks svg{position:absolute;left:0;top:3px;width:15px;height:15px}

/* logos */
.center-title{left:0;width:1200px;text-align:center}
.logo-row{left:142px;width:918px;height:86px;display:flex;gap:13px}
.logo-box{flex:1;border:1px solid var(--line);background:var(--white);display:flex;align-items:center;justify-content:center;gap:7px;font-weight:700;font-size:19px;color:#444}
.logo-box.picked{border-color:var(--orange)}
.mark{width:12px;height:12px;background:#444;border-radius:50%}
.mark.sq{border-radius:0}

/* technicians */
.tech-band{left:0;top:1525px;width:1200px;height:595px;background:var(--cream);clip-path:polygon(0 0,100% 5%,100% 100%,0 100%)}
.tech-card{top:1717px;width:438px;height:255px;background:var(--white);padding:18px 26px}
.tech-head{display:flex;align-items:center;gap:12px;margin-bottom:14px}
.avatar{width:60px;height:60px;border-radius:50%;background:linear-gradient(160deg,#d9c2a8,#8e7a68);border:3px solid #eee}
.tech-name{color:var(--orange);font-weight:500;font-size:14px}
.tech-role{font-size:11.5px;color:#777;margin-top:3px}
.stars{color:var(--orange);font-size:13px;letter-spacing:1px}
.tech-loc{font-size:11.5px;color:#777;margin:8px 0 14px}
.tech-text{font-size:11.5px;line-height:20px;color:#777}
.read-more{display:inline-block;margin-top:12px;font-size:12px;color:#666;text-decoration:underline}
.dots{left:578px;top:2011px;display:flex;gap:6px}
.dot{width:9px;height:9px;border-radius:50%;border:1px solid #999;background:var(--white)}
.dot.on{background:var(--orange);border-color:var(--orange)}

/* cities */
.cities-band{left:0;top:2410px;width:1200px;height:632px;background:var(--mist);clip-path:polygon(0 4%,100% 0,100% 100%,0 100%)}
.map{left:140px;top:2580px;width:523px;height:368px;border:2px solid var(--orange);background:linear-gradient(135deg,#eeeeee,#e2e2e2 60%,#ebebeb)}
.state{font-size:17px;color:#666;display:flex;align-items:center;gap:10px}
.state::before{content:"";width:5px;height:5px;border-radius:50%;background:#888}

/* cta */
.cta-title{left:142px;top:3166px;font-family:'Roboto Condensed',sans-serif;font-style:italic;font-weight:700;font-size:40px;color:#555}
.cta-sub{left:142px;top:3223px;font-family:'Roboto Condensed',sans-serif;font-style:italic;font-size:21px;color:#777}
.cta-btn{left:142px;top:3271px;width:140px;height:41px;font-size:14px}
.cta-art{left:442px;top:3080px;width:564px;height:405px;background:radial-gradient(ellipse at 50% 55%,#dfe2ea 0%,#cdd4e6 40%,rgba(255,255,255,0) 72%)}

/* footer */
.footer{left:0;top:3576px;width:1200px;height:310px;background:linear-gradient(180deg,#35383c,#24262a);clip-path:polygon(0 0,100% 3%,100% 100%,0 100%)}
.f-col{top:3642px;color:var(--white)}
.f-col h4{font-size:17px;font-weight:500;margin-bottom:8px}
.f-col ul{list-style:none}
.f-col li{font-size:12.5px;line-height:28px;color:#e6e6e6}
.f-col li::before{content:"›";margin-right:8px}
.social li{display:flex;align-items:center;gap:12px;line-height:44px;font-style:italic}
.social li::before{content:none}
.ring{width:28px;height:28px;border:1.5px solid #ddd;border-radius:50%}
.copyright{left:0;top:3886px;width:1200px;height:43px;background:var(--orange);color:var(--white);font-size:12px;display:flex;align-items:center;justify-content:center}
</style>
</head>
<body>

<header class="abs site-header">
  <div class="abs brand"><span class="brand-mark"></span>Bolt Handy</div>
  <a class="abs nav active" style="left:566px">Home</a>
  <a class="abs nav" style="left:632px">About Us</a>
  <a class="abs nav" style="left:719px">Contact Us</a>
  <a class="abs nav" style="left:818px">Areas Served</a>
  <a class="abs nav" style="left:929px">Pricing And Services</a>
</header>

<section>
  <div class="abs hero-bg"></div>
  <div class="abs hero-photo" role="img" aria-label="Photo of a smiling family of four waving at a laptop"></div>
  <h1 class="abs hero-title">We do Installation,<br>Repairs And Smart<br>Home</h1>
  <a class="abs btn hero-btn">Book A Service</a>
</section>

<nav class="abs services">
  <div class="service">
    <svg viewBox="0 0 46 46" fill="none" stroke="#444" stroke-width="2"><rect x="14" y="6" width="18" height="34" rx="3"/><line x1="20" y1="35" x2="26" y2="35"/></svg>
    Phone Repair
  </div>
  <div class="service">
    <svg viewBox="0 0 46 46" fill="none" stroke="#444" stroke-width="2"><rect x="5" y="8" width="36" height="24" rx="2"/><line x1="16" y1="38" x2="30" y2="38"/><line x1="23" y1="32" x2="23" y2="38"/></svg>
    TV Mounting
  </div>
  <div class="service current">
    <svg viewBox="0 0 46 46" fill="none" stroke="#f7941d" stroke-width="2"><rect x="8" y="10" width="28" height="12" rx="2" transform="rotate(15 22 16)"/><circle cx="32" cy="19" r="3"/><path d="M18 24 L16 34 H8"/></svg>
    Security Camera<br>Installation
  </div>
  <div class="service">
    <svg viewBox="0 0 46 46" fill="none" stroke="#444" stroke-width="2"><rect x="6" y="26" width="34" height="10" rx="2"/><line x1="12" y1="26" x2="10" y2="8"/><line x1="34" y1="26" x2="36" y2="8"/><path d="M17 18 a8 8 0 0 1 12 0"/><path d="M20 21 a4 4 0 0 1 6 0"/></svg>
    Networking / Wi-Fi
  </div>
  <div class="service">
    <svg viewBox="0 0 46 46" fill="none" stroke="#444" stroke-width="2"><path d="M6 22 L23 8 L40 22"/><rect x="11" y="21" width="24" height="17"/><rect x="19" y="28" width="8" height="10"/></svg>
    Smart Home<br>Services
  </div>
  <div class="service">
    <svg viewBox="0 0 46 46" fill="none" stroke="#444" stroke-width="2"><rect x="6" y="6" width="34" height="28" rx="2"/><line x1="14" y1="14" x2="32" y2="28"/><line x1="32" y1="14" x2="14" y2="28"/><path d="M14 34 L12 42 L20 36"/></svg>
    IT Support
  </div>
</nav>

<section>
  <div class="abs house-photo" role="img" aria-label="Photo of a two-storey suburban house with a green lawn"></div>
  <div class="abs about-card">
    <h2 class="section-title">A Simple Way To Take<br>Care of Everything</h2>
    <ul class="ticks">
      <li><svg viewBox="0 0 16 16" fill="none" stroke="#f7941d" stroke-width="1.5"><circle cx="8" cy="8" r="6.5"/><path d="M5 8 L7.3 10.3 L11 6"/></svg>Trusted Technicians In Your<br>Neighborhood</li>
      <li><svg viewBox="0 0 16 16" fill="none" stroke="#f7941d" stroke-width="1.5"><circle cx="8" cy="8" r="6.5"/><path d="M5 8 L7.3 10.3 L11 6"/></svg>Guaranteed parts and service + 24/7<br>support</li>
      <li><svg viewBox="0 0 16 16" fill="none" stroke="#f7941d" stroke-width="1.5"><circle cx="8" cy="8" r="6.5"/><path d="M5 8 L7.3 10.3 L11 6"/></svg>Hundreds of repair and install options</li>
    </ul>
  </div>
</section>

<section>
  <h2 class="abs center-title section-title" style="top:1295px">Trusted By</h2>
  <div class="abs logo-row" style="top:1369px">
    <div class="logo-box"><span class="mark"></span>veridan</div>
    <div class="logo-box">HALVORA</div>
    <div class="logo-box">Norrel Co</div>
    <div class="logo-box"><span class="mark sq"></span>Greenmoor</div>
    <div class="logo-box picked">Aquilon</div>
    <div class="logo-box"><span class="mark"></span>Stellwise</div>
  </div>
</section>

<section>
  <div class="abs tech-band"></div>
  <h2 class="abs center-title section-title" style="top:1631px">Our Top Technicians Are In Your Neighborhood And Beyond</h2>
  <article class="abs tech-card" style="left:142px">
    <div class="tech-head"><div class="avatar" role="img" aria-label="Technician portrait"></div><div><div class="tech-name">Mara Lindqvist</div><div class="tech-role">Bolt Handy Technician</div></div></div>
    <div class="stars">★★★★★</div>
    <div class="tech-loc">Celia | Los Angeles, CA</div>
    <p class="tech-text">Lorem ipsum dolor sit amet, consectetur adipis elit donec vel enim a dui fermentum semper ut volutpat blandit orci, eget sodales sapien scele risqued sit amet vestibulum ante.</p>
    <a class="read-more">Read More</a>
  </article>
  <article class="abs tech-card" style="left:621px">
    <div class="tech-head"><div class="avatar" role="img" aria-label="Technician portrait"></div><div><div class="tech-name">Theo Barrow</div><div class="tech-role">Bolt Handy Technician</div></div></div>
    <div class="stars">★★★★★</div>
    <div class="tech-loc">Rowan | Colton, CA</div>
    <p class="tech-text">Lorem ipsum dolor sit amet, consectetur adipis elit donec vel enim a dui fermentum semper ut volutpat blandit orci, eget sodales sapien scele risqued sit amet vestibulum ante.</p>
    <a class="read-more">Read More</a>
  </article>
  <div class="abs dots"><span class="dot"></span><span class="dot on"></span><span class="dot"></span></div>
</section>

<section>
  <h2 class="abs center-title section-title" style="top:2184px">Featured In</h2>
  <div class="abs logo-row" style="top:2258px">
    <div class="logo-box"><span class="mark sq"></span>Quorvo</div>
    <div class="logo-box">brinket</div>
    <div class="logo-box picked">Tallow.net</div>
    <div class="logo-box">Lumora</div>
    <div class="logo-box">cinder</div>
    <div class="logo-box"><span class="mark sq"></span>Retail Forum</div>
  </div>
</section>

<section>
  <div class="abs cities-band"></div>
  <h2 class="abs center-title section-title" style="top:2510px">Cities Where Bolt Handy Is Available</h2>
  <div class="abs map" role="img" aria-label="Map of the western United States with orange pins on served cities"></div>
  <div class="abs state" style="left:717px;top:2608px">Arizona</div>
  <div class="abs state" style="left:717px;top:2653px">Colorado</div>
  <div class="abs state" style="left:717px;top:2698px">Florida</div>
  <div class="abs state" style="left:717px;top:2744px">Georgia</div>
  <div class="abs state" style="left:717px;top:2789px">Illinois</div>
  <div class="abs state" style="left:717px;top:2835px">Massachusetts</div>
  <div class="abs state" style="left:901px;top:2608px">Nevada</div>
  <div class="abs state" style="left:901px;top:2653px">North Carolina</div>
  <div class="abs state" style="left:901px;top:2698px">Pennsylvania</div>
  <div class="abs state" style="left:901px;top:2744px">Texas</div>
  <div class="abs state" style="left:901px;top:2789px">Washington D.C.</div>
</section>

<section>
  <div class="abs cta-art" role="img" aria-label="Illustration of a white service van and two technicians in blue overalls carrying toolboxes"></div>
  <h2 class="abs cta-title">Ready To Get Started?</h2>
  <p class="abs cta-sub">Repair Or Install A Device Today.</p>
  <a class="abs btn cta-btn">Book A Service</a>
</section>

<footer>
  <div class="abs footer"></div>
  <div class="abs f-col" style="left:142px"><h4>Quick Links</h4><ul><li>Home</li><li>About Us</li><li>Contact Us</li><li>Areas Served</li><li>Pricing &amp; Services</li></ul></div>
  <div class="abs f-col" style="left:386px"><h4>Resources</h4><ul><li>Phone Repair</li><li>TV Mounting</li><li>Security Camera Installation</li><li>Networking / Wi-Fi</li><li>Smart Home Services</li><li>IT Support</li></ul></div>
  <div class="abs f-col" style="left:689px"><h4>Legals</h4><ul><li>Privacy</li><li>Terms &amp; Conditions</li><li>Guarantee</li></ul></div>
  <div class="abs f-col" style="left:942px"><h4>Follow Us On</h4><ul class="social"><li><span class="ring"></span>Facelane</li><li><span class="ring"></span>Chirper</li><li><span class="ring"></span>Viewtube</li></ul></div>
  <div class="abs copyright">Copyright © 2020 Bolt Handy. All Rights Reserved.</div>
</footer>

</body>
</html>
```